Banner Design Childcare Centre Landscape Orientation

Design a 3000 x 1500mm landscape orientation(using attached template Template - Outdoor-Banner-Large-1500x3000_PORTRAIT ***But please change to landscape orientation) to include these information:

Logo

Slogan = Empowering tomorrow's leaders with confidence, independence, creativity and a strong passion for learning.

- Ages 6 weeks to 6 years
- STEAM based educational programs with a focus on the Montessori method

Now Enrolling
www.brightspa.com.au
02 64170259
17 Harlow Road, Lidcombe NSW 2141

***Please also include a qr code on the design that directs to www.brightspa.com.au
____________________________

About us:

Main Colour Scheme (can add other colours to make it appealing)
The colour scheme for our brand will be HEX #FFFFFF (white), #000000 (black), #F7931A (orange) , #4D4D4D (grey), #00AEFF (blue), #00CAFE (lighter blue).

- Our Mission
The mission of BRIGHT Sprout Play Academy is to be a leading educational academy for students of infant, toddler and preschool age (1-6 years old). We aim to promote confidence, independence, responsibility, creativity and a strong passion for learning via STEAM (Science, Technology, Engineering, Arts and Mathematics) based education built on a foundation of Montessori principles.

Why STEAM based education via Montessori Principles
Why STEAM based education?

The development of critical thinking skills in students is crucial to preparing them for the challenges of the future. Encouraging students of all ages to think deeply and approach problems with a creative and innovative mindset is essential to fostering the next generation of leaders, innovators, and educators. The integration of Science, Technology, Engineering, Art, and Mathematics (STEAM) in education provides students with a well-rounded and hands-on approach to learning, inspiring them to think more broadly and solve problems with a real-world focus.

Through the implementation of STEAM-based education, students can progress from project-based learning, where they collaborate to explore and discover, to problem-based learning, where they focus on real-world challenges, and ultimately to place-based learning, where they learn by doing. This approach ensures that students are not only gaining knowledge and skills, but also developing their ability to think critically and creatively.

It is equally important to emphasise the role of the arts in education, as creativity and innovation are key components of the future workforce. By providing opportunities for students to apply their knowledge and skills in practical and applicable ways, the arts can support STEAM-based education and ensure that all students are ready to face the challenges ahead.

STEAM-based education provides a comprehensive and hands-on approach to learning, equipping students with the critical thinking and problem-solving skills they will need to succeed in the future. Every child should have the opportunity to develop their creative and innovative abilities, regardless of their career path, and STEAM education is an effective means of achieving this goal.

Why focus on the Montessori Method?

The Montessori Method provides a comprehensive approach to child development and education, offering numerous benefits for children who are raised within its principles. This method is well known for its individualised approach to learning, which allows students to progress at their own pace, and its focus on fostering independence.

In addition to these well-established benefits, the Montessori Method also places a strong emphasis on empathy, social justice, and a lifelong love of learning. By providing children with the freedom and support to question, explore, and make connections, Montessori students develop into confident, enthusiastic, and self-directed learners. They acquire the critical thinking, collaboration, and boldness that are vital skills for children to be well-rounded, confident, and effective leaders in the 21st century.

Industry/Entity Type

Childcare centre

Requirements
Must have
• Landscape orientation (1500 high, 3000 wide)

```html
<!DOCTYPE html>
<html lang="en">
<head>
<meta charset="utf-8">
<title>BRIGHT Sprout Play Academy – Now Enrolling Banner</title>
<link rel="stylesheet" href="https://fonts.googleapis.com/css2?family=Lilita+One&family=Montserrat:wght@600;700;800&display=swap">
<style>
  :root {
    --page: #e6e6e6;
    --blue-deep: #1872ad;
    --blue-mid: #1b8fcc;
    --blue-bright: #22aee3;
    --sky-pill: #e9f5fc;
    --yellow: #fff170;
    --yellow-text: #fff35c;
    --orange: #f7931a;
    --blue-text: #2a9be0;
    --grey-text: #3d3d3d;
    --white: #ffffff;
    --grass: #5cbf4f;
  }
  * { box-sizing: border-box; margin: 0; padding: 0; }
  html, body {
    width: 1200px; height: 875px; overflow: hidden;
    background: var(--page);
  }
  .banner {
    position: absolute; left: 0; top: 137px;
    width: 1200px; height: 600px; overflow: hidden;
    background: linear-gradient(180deg, var(--blue-deep) 0%, var(--blue-mid) 55%, var(--blue-bright) 100%);
    font-family: "Montserrat", sans-serif;
  }
  .art { position: absolute; left: 0; top: 0; width: 1200px; height: 600px; }

  .headline {
    position: absolute; left: 44px; top: 36px;
    font-family: "Lilita One", sans-serif; font-weight: 400;
    color: var(--white); font-size: 45px; line-height: 56px;
    letter-spacing: 0.3px; text-transform: uppercase; white-space: nowrap;
  }
  .values {
    position: absolute; left: 42px; top: 150px;
    font-family: "Lilita One", sans-serif;
    color: var(--yellow-text); font-size: 34px; line-height: 38px;
    text-transform: uppercase; white-space: nowrap;
  }
  .passion {
    position: absolute; left: 42px; top: 227px;
    color: var(--white); font-weight: 700; font-size: 22.5px;
    text-transform: uppercase; letter-spacing: 0.3px; white-space: nowrap;
  }

  .pill {
    position: absolute; left: 40px; width: 548px; border-radius: 30px;
    box-shadow: 7px 3px 0 #2f8fd1;
  }
  .pill-ages {
    top: 271px; height: 55px; background: var(--sky-pill);
    font-weight: 800; font-size: 31px; letter-spacing: -0.3px;
    text-transform: uppercase; padding-left: 41px; line-height: 55px; white-space: nowrap;
  }
  .pill-ages .orange { color: var(--orange); }
  .pill-ages .blue { color: var(--blue-text); }
  .pill-programs {
    top: 340px; height: 56px; background: var(--yellow);
    padding: 8px 0 0 39px; font-weight: 700; font-size: 15.5px;
    line-height: 20px; color: var(--grey-text);
  }
  .pill-programs .blue { color: var(--blue-text); font-weight: 800; }

  .brand {
    position: absolute; left: 34px; top: 462px; width: 140px;
    text-align: center; color: var(--orange);
    font-weight: 700; font-size: 14px; line-height: 17px;
  }
  .brand-mark {
    width: 56px; height: 56px; border-radius: 50%;
    background: #f4dcb8; margin: 0 auto 8px;
  }

  .contact { position: absolute; left: 206px; list-style: none; }
  .contact li {
    position: absolute; left: 0; display: flex; align-items: center;
    white-space: nowrap; color: var(--white); font-weight: 700;
  }
  .icon {
    width: 40px; height: 40px; border-radius: 50%; background: var(--white);
    display: flex; align-items: center; justify-content: center;
    flex: none; margin-right: 18px;
  }
  .contact .phone { top: 424px; }
  .contact .phone span { color: var(--yellow-text); font-size: 40px; font-weight: 800; letter-spacing: 0.5px; }
  .contact .address { top: 472px; font-size: 16.5px; }
  .contact .web { top: 516px; font-size: 16.5px; }

  .enrolling {
    position: absolute; left: 620px; top: 296px; width: 208px; height: 208px;
    text-align: center; font-family: "Lilita One", sans-serif;
  }
  .enrolling .now {
    position: absolute; left: 0; right: 0; top: 52px;
    color: var(--sky-pill); font-size: 66px; line-height: 60px;
  }
  .enrolling .enrol {
    position: absolute; left: 0; right: 0; top: 112px;
    color: var(--yellow-text); font-size: 27px; line-height: 28px;
  }
</style>
</head>
<body>
<main class="banner">
  <svg class="art" viewBox="0 0 1200 600" aria-hidden="true">
    <path d="M600,220 C600,110 720,12 900,0 L925,0 C1060,20 1160,80 1200,140 L1200,600 L1130,600 C1000,560 900,420 760,380 C680,360 604,300 600,220 Z" fill="#ffffff"/>
    <path d="M0,586 C300,578 700,580 1200,590 L1200,600 L0,600 Z" fill="var(--grass)"/>
  </svg>

  <div role="img" aria-label="Three wax crayons in green, yellow and pink hanging from the top edge"
       style="position:absolute;left:446px;top:0;width:96px;height:57px;background:linear-gradient(90deg,#2f9d4a 0 30%,transparent 30% 36%,#f2c51c 36% 64%,transparent 64% 70%,#d8336f 70%);opacity:.85;border-radius:0 0 10px 10px;"></div>

  <div role="img" aria-label="Crumpled yellow paper light bulb with drawn rays of light"
       style="position:absolute;left:640px;top:70px;width:240px;height:226px;border-radius:50%;background:radial-gradient(circle, #f5dd2a 0 28%, #fbf3b0 42%, rgba(255,255,255,0) 70%);"></div>

  <div role="img" aria-label="Two folded paper planes"
       style="position:absolute;left:1050px;top:28px;width:130px;height:120px;background:linear-gradient(135deg,#d7dee3,rgba(255,255,255,0) 70%);border-radius:40% 10% 50% 20%;"></div>

  <div role="img" aria-label="Young boy in a yellow shirt lying on the floor building a toy car from colourful plastic bricks"
       style="position:absolute;left:790px;top:115px;width:410px;height:485px;background:linear-gradient(160deg,#a47a55 0%,#f5d77e 40%,#ecc762 70%,#e8503a 88%,#3a7fd0 100%);border-radius:46% 0 0 30% / 40% 0 0 20%;"></div>

  <h1 class="headline">Empowering<br>Tomorrow’s Leaders</h1>
  <p class="values">With confidence, independence,<br>creativity and</p>
  <p class="passion">A strong passion for learning.</p>

  <div class="pill pill-ages">
    <span class="orange">Ages</span> <span class="blue">6 weeks</span> <span class="orange">to</span> <span class="blue">6 years</span>
  </div>
  <div class="pill pill-programs">
    <span class="blue">STEAM</span> based educational programs with a focus on<br>the Montessori method
  </div>

  <div class="brand">
    <div class="brand-mark"></div>
    BRIGHT Sprout Play Academy
  </div>

  <ul class="contact">
    <li class="phone">
      <span class="icon"><svg width="22" height="22" viewBox="0 0 24 24"><path d="M6.6 2.5l3 3.4-1.8 2.4c1.2 2.6 3.3 4.7 5.9 5.9l2.4-1.8 3.4 3-1.6 3.6C10.5 19 5 13.5 3 6.1z" fill="var(--blue-text)"/></svg></span>
      <span>02 64170259</span>
    </li>
    <li class="address">
      <span class="icon"><svg width="20" height="22" viewBox="0 0 24 26"><path d="M12 1a8 8 0 0 0-8 8c0 6 8 15 8 15s8-9 8-15a8 8 0 0 0-8-8zm0 11a3 3 0 1 1 0-6 3 3 0 0 1 0 6z" fill="var(--blue-text)"/></svg></span>
      17 Harlow Road, Lidcombe NSW 2141
    </li>
    <li class="web">
      <span class="icon"><svg width="22" height="22" viewBox="0 0 24 24" fill="none" stroke="var(--blue-text)" stroke-width="2"><circle cx="12" cy="12" r="9"/><ellipse cx="12" cy="12" rx="4" ry="9"/><path d="M3 12h18M5 7h14M5 17h14"/></svg></span>
      www.brightspa.com.au
    </li>
  </ul>

  <div class="enrolling">
    <svg width="208" height="208" viewBox="-104 -104 208 208" aria-hidden="true">
      <polygon fill="var(--orange)" stroke="#ffffff" stroke-width="3"
        points="104,0 78.5,15.6 96.1,39.8 66.5,44.5 73.5,73.5 44.5,66.5 39.8,96.1 15.6,78.5 0,104 -15.6,78.5 -39.8,96.1 -44.5,66.5 -73.5,73.5 -66.5,44.5 -96.1,39.8 -78.5,15.6 -104,0 -78.5,-15.6 -96.1,-39.8 -66.5,-44.5 -73.5,-73.5 -44.5,-66.5 -39.8,-96.1 -15.6,-78.5 0,-104 15.6,-78.5 39.8,-96.1 44.5,-66.5 73.5,-73.5 66.5,-44.5 96.1,-39.8 78.5,-15.6"/>
    </svg>
    <div class="now">NOW</div>
    <div class="enrol">ENROLLING</div>
  </div>
</main>
</body>
</html>
```